Become a Mentor - For Musicians, Artists, Producers and Teachers

Here is the full creative brief:

https://sheets.plorvex.com/grids/d/9kTmWqRz4_PLbN2sYhC8vXeJ3uKdAfG7nLoQwErTpMzb/view?src=shared

Here is the background image file: https://www.filquarry.com/fs/83tbwmynq4kpz/BBLs7h2QNF8PcTwXX-mk3RUVb?get=0

LOGO:
https://www.filquarry.com/fs/w472mujakd8n5/BBCK6TueRP3Z-hVLwYnZ1Xbba?get=0

```html
<!DOCTYPE html>
<html lang="en">
<head>
<meta charset="utf-8">
<title>Become a Mentor – Banner Set</title>
<link rel="stylesheet" href="https://fonts.googleapis.com/css2?family=Josefin+Sans:wght@300;400&family=Montserrat:wght@600;700&family=Maven+Pro:wght@600;700&display=swap">
<style>
  :root {
    --board: #dcdcdc;
    --banner-bg: #050505;
    --pink: #f06b80;
    --white: #ffffff;
    --apply-blue: #1437d6;
    --url-pink: #f0207a;
    --studio-dark: #15101c;
    --studio-violet: #7a3fb8;
    --studio-blue: #2a4fd0;
    --studio-magenta: #d84fa8;
    --studio-warm: #b98c62;
  }
  * { margin: 0; padding: 0; box-sizing: border-box; }
  html, body { width: 1200px; height: 499px; overflow: hidden; background: var(--board); }
  .board { position: relative; width: 1200px; height: 499px; }

  .banner { position: absolute; background: var(--banner-bg); overflow: hidden; box-shadow: 0 1px 3px rgba(0,0,0,.25); }
  .banner--leaderboard { left: 49px; top: 124px; width: 244px; height: 93px; }
  .banner--wide { left: 49px; top: 242px; width: 322px; height: 169px; }
  .banner--square { left: 412px; top: 89px; width: 322px; height: 323px; }
  .banner--photo { left: 793px; top: 124px; width: 358px; height: 268px; }

  .studio-photo {
    position: absolute;
    background:
      radial-gradient(ellipse 30% 35% at 25% 70%, rgba(240,230,215,.85), transparent 70%),
      radial-gradient(ellipse 25% 40% at 75% 72%, rgba(60,45,40,.9), transparent 70%),
      radial-gradient(ellipse 35% 30% at 55% 35%, rgba(216,79,168,.75), transparent 70%),
      radial-gradient(ellipse 40% 35% at 80% 25%, rgba(42,79,208,.8), transparent 70%),
      radial-gradient(ellipse 30% 30% at 15% 30%, rgba(122,63,184,.8), transparent 70%),
      linear-gradient(180deg, var(--studio-dark) 0%, #3a2350 45%, #4a3a32 75%, #1b1714 100%);
  }
  .banner--leaderboard .studio-photo { left: 0; top: 0; width: 160px; height: 93px;
    -webkit-mask-image: linear-gradient(90deg, #000 70%, transparent 100%); mask-image: linear-gradient(90deg, #000 70%, transparent 100%); }
  .banner--wide .studio-photo { left: 0; top: 0; width: 250px; height: 169px;
    -webkit-mask-image: linear-gradient(120deg, #000 55%, transparent 85%); mask-image: linear-gradient(120deg, #000 55%, transparent 85%); }
  .banner--square .studio-photo { left: 0; top: 85px; width: 322px; height: 238px;
    -webkit-mask-image: linear-gradient(180deg, transparent 0%, #000 25%); mask-image: linear-gradient(180deg, transparent 0%, #000 25%); }
  .banner--photo .studio-photo { left: 0; top: 0; width: 358px; height: 268px; }

  .copy { position: absolute; text-align: center; color: var(--white); }
  .tagline { font-family: "Josefin Sans", sans-serif; font-weight: 400; color: var(--pink); letter-spacing: .08em; white-space: nowrap; }
  .lead-in { font-family: "Josefin Sans", sans-serif; font-weight: 300; letter-spacing: .35em; white-space: nowrap; }
  .headline { font-family: "Montserrat", sans-serif; font-weight: 700; line-height: 1; letter-spacing: .01em; white-space: nowrap;
    -webkit-text-stroke: 0.6px var(--banner-bg); }
  .apply { display: inline-block; background: var(--apply-blue); font-family: "Maven Pro", sans-serif; font-weight: 600; letter-spacing: .04em; line-height: 1.2; }
  .phone { font-family: "Maven Pro", sans-serif; font-weight: 700; white-space: nowrap; line-height: 1; }
  .web { font-family: "Maven Pro", sans-serif; font-weight: 600; color: var(--url-pink); white-space: nowrap; }

  /* leaderboard */
  .banner--leaderboard .copy { right: 10px; top: 7px; width: 100px; }
  .banner--leaderboard .tagline { font-size: 6.2px; }
  .banner--leaderboard .lead-in { font-size: 5.8px; margin-top: 5px; }
  .banner--leaderboard .headline { font-size: 21px; margin-top: 2px; }
  .banner--leaderboard .cta { position: absolute; right: 10px; top: 65px; text-align: right; }
  .banner--leaderboard .apply { font-size: 4px; padding: 0 3px; }
  .banner--leaderboard .phone { font-size: 8.6px; margin-top: 3px; }
  .banner--leaderboard .web { font-size: 3.6px; margin-top: 1px; }

  /* wide */
  .banner--wide .copy { right: 11px; top: 10px; width: 150px; }
  .banner--wide .tagline { font-size: 9.4px; }
  .banner--wide .lead-in { font-size: 8.6px; margin-top: 9px; }
  .banner--wide .headline { font-size: 33px; margin-top: 4px; }
  .banner--wide .glow { position: absolute; right: 0; bottom: 0; width: 180px; height: 80px;
    background: radial-gradient(ellipse at 30% 100%, rgba(30,110,30,.55), transparent 65%), radial-gradient(ellipse at 50% 40%, rgba(120,20,30,.35), transparent 70%); }
  .banner--wide .cta { position: absolute; right: 14px; top: 123px; text-align: right; }
  .banner--wide .apply { font-size: 7.2px; padding: 1px 4px; }
  .banner--wide .phone { font-size: 15px; margin-top: 5px; }
  .banner--wide .web { font-size: 6.4px; margin-top: 2px; }

  /* square */
  .banner--square .copy { left: 0; top: 22px; width: 322px; }
  .banner--square .tagline { font-size: 12.5px; }
  .banner--square .lead-in { font-size: 11px; margin-top: 12px; }
  .banner--square .headline { font-size: 44px; margin-top: 8px; }
</style>
</head>
<body>
<main class="board">

  <section class="banner banner--leaderboard">
    <div class="studio-photo" role="img" aria-label="Mentor and student talking in a recording studio with neon music visuals"></div>
    <div class="copy">
      <p class="tagline">START YOUR CAREER TODAY</p>
      <p class="lead-in">BECOME A</p>
      <h2 class="headline">MENTOR</h2>
    </div>
    <div class="copy cta">
      <span class="apply">APPLY NOW</span>
      <p class="phone">CALL 1300 555 014</p>
      <p class="web">www.harbourlinemusic.com.au</p>
    </div>
  </section>

  <section class="banner banner--wide">
    <div class="studio-photo" role="img" aria-label="Mentor and student talking in a recording studio with neon music visuals"></div>
    <div class="glow"></div>
    <div class="copy">
      <p class="tagline">START YOUR CAREER TODAY</p>
      <p class="lead-in">BECOME A</p>
      <h2 class="headline">MENTOR</h2>
    </div>
    <div class="copy cta">
      <span class="apply">APPLY NOW</span>
      <p class="phone">CALL 1300 555 014</p>
      <p class="web">www.harbourlinemusic.com.au</p>
    </div>
  </section>

  <section class="banner banner--square">
    <div class="studio-photo" role="img" aria-label="Mentor and student talking in a recording studio with neon music visuals"></div>
    <div class="copy">
      <p class="tagline">START YOUR CAREER TODAY</p>
      <p class="lead-in">BECOME A</p>
      <h2 class="headline">MENTOR</h2>
    </div>
  </section>

  <section class="banner banner--photo">
    <div class="studio-photo" role="img" aria-label="Mentor and student talking in a recording studio with neon music visuals"></div>
  </section>

</main>
</body>
</html>
```